Tour agency for FIT and groups need a business card design

We need a business card design for a tour agency company that is based in Perth called" BRISK NO", we aim to provide customise, unique and seamless travel arrangement for FIT and groups. We serve both high profile businessperson, government authorities, business partners, executives and investors. The name card should be more professional looking.
Updates

Project Deadline Extended Reason: Have some changes that needed to make, director will be back to office on Monday, sorry for the inconvenience cause. Added Saturday, May 6, 2017

Target Market(s)

High profile businessperson, government authorities, business partners, executives and investors.

Industry/Entity Type

Tourism

Contact Information for Business Card

Brisk NO
Level 1, 214 Marlowe Avenue, Dunreath NO, 6120
www.briskno.com.au

Font styles to use
Serif

Colors

Designer to choose colors to be used in the design.

Requirements
Must have
• My project must have a company logo
Nice to have
• a more professional and solid yet friendly name card design. We may want to include chinese name in the name card as well. Edge of the card can be filled with gold and we think that transparent name cards are interesting.

```html
<!DOCTYPE html>
<html lang="en">
<head>
<meta charset="utf-8">
<title>Brisk NO – Business Card</title>
<link rel="stylesheet" href="https://fonts.googleapis.com/css2?family=Raleway:wght@300;400;500;600;700&display=swap">
<style>
  :root {
    --stage: #000000;
    --navy: #2e2a6e;
    --blue: #0b6fb8;
    --mid-blue: #1f4f93;
    --green: #8cc63f;
    --green-dark: #0b7a3b;
    --shadow-navy: #13284f;
    --white: #ffffff;
    --name-blue: #1d5ea8;
    --ink: #3a3a3a;
  }
  * { margin: 0; padding: 0; box-sizing: border-box; }
  html, body {
    width: 1200px; height: 1200px; overflow: hidden;
    background: var(--stage);
    font-family: "Raleway", sans-serif;
  }
  .card {
    position: absolute; left: 363px; width: 475px; height: 285px; overflow: hidden;
  }
  .card--front {
    top: 165px;
    background: linear-gradient(90deg, var(--navy) 0%, var(--mid-blue) 50%, var(--blue) 100%);
  }
  .front-art { position: absolute; inset: 0; }
  .brand-tab {
    position: absolute; left: 93px; top: 86px; width: 287px; height: 101px;
    border-radius: 26px; background: var(--green);
    box-shadow: 0 4px 10px rgba(0,0,0,.35);
    text-align: center;
  }
  .brand-name {
    position: absolute; left: 0; right: 0; top: 34px;
    font-size: 34px; font-weight: 700; color: var(--navy); letter-spacing: 1px;
  }
  .brand-url {
    position: absolute; left: 0; right: 0; top: 79px;
    font-size: 13px; font-weight: 400; color: var(--white);
  }

  .card--back { top: 479px; background: var(--white); }
  .back-art { position: absolute; inset: 0; }
  .person {
    position: absolute; left: 59px; top: 142px;
    transform: translate(-50%, -50%) rotate(-90deg);
    white-space: nowrap; text-align: left;
  }
  .person-name { font-size: 26px; font-weight: 400; color: var(--name-blue); line-height: 1; }
  .person-role { font-size: 15px; font-weight: 300; color: var(--ink); line-height: 1.1; padding-left: 2px; }
  .mini-tab {
    position: absolute; left: 158px; top: 76px; width: 40px; height: 134px;
    border-radius: 10px; background: var(--green);
    box-shadow: 0 3px 8px rgba(0,0,0,.35);
  }
  .mini-tab-name {
    position: absolute; left: 50%; top: 50%;
    transform: translate(-50%, -50%) rotate(-90deg);
    font-size: 14px; font-weight: 700; color: var(--navy); white-space: nowrap;
  }
  .contacts { position: absolute; left: 242px; top: 0; }
  .contact {
    position: absolute; left: 0; display: flex; align-items: flex-start; gap: 11px;
    color: var(--white); font-size: 12.5px; font-weight: 500; line-height: 1.2; white-space: nowrap;
  }
  .contact svg { flex: none; width: 24px; height: 24px; }
  .contact span { padding-top: 4px; }
</style>
</head>
<body>

<section class="card card--front" aria-label="Card front">
  <svg class="front-art" width="475" height="285" viewBox="0 0 475 285" aria-hidden="true">
    <rect class="band" x="0" y="120" width="475" height="103" fill="#8cc63f"/>
    <rect class="band-shadow" x="134" y="150" width="205" height="73" fill="#13284f"/>
    <polygon class="fold" points="93,150 134,187 134,223" fill="#0b7a3b"/>
    <polygon class="fold" points="380,150 339,187 339,223" fill="#0b7a3b"/>
  </svg>
  <div class="brand-tab">
    <div class="brand-name">Brisk NO</div>
    <div class="brand-url">www.briskno.com.au</div>
  </div>
</section>

<section class="card card--back" aria-label="Card back">
  <svg class="back-art" width="475" height="285" viewBox="0 0 475 285" aria-hidden="true">
    <defs>
      <linearGradient id="backBlue" x1="0" x2="1" y1="0" y2="0">
        <stop offset="0" stop-color="#1f4f93"/>
        <stop offset="1" stop-color="#0b6fb8"/>
      </linearGradient>
    </defs>
    <rect class="panel" x="211" y="0" width="264" height="285" fill="url(#backBlue)"/>
    <rect class="strip" x="171" y="0" width="40" height="285" fill="#8cc63f"/>
    <rect class="strip-shadow" x="198" y="95" width="13" height="96" fill="#13284f"/>
    <polygon class="fold" points="198,80 211,95 198,95" fill="#0b7a3b"/>
    <polygon class="fold" points="198,206 211,191 198,191" fill="#0b7a3b"/>
  </svg>

  <div class="person">
    <div class="person-name">lena ford</div>
    <div class="person-role">accountant</div>
  </div>

  <div class="mini-tab"><div class="mini-tab-name">Brisk NO</div></div>

  <div class="contacts">
    <div class="contact" style="top:92px">
      <svg viewBox="0 0 24 24" aria-hidden="true"><circle cx="12" cy="12" r="12" fill="#8cc63f"/>
        <path d="M8.2 6.5l2 2.3-1.1 1.5c.8 1.7 2 2.9 3.6 3.7l1.5-1.1 2.3 2-1.2 1.9c-4.1-.4-7.6-3.9-8-8z" fill="#fff"/></svg>
      <span>08 6300 4172</span>
    </div>
    <div class="contact" style="top:130px">
      <svg viewBox="0 0 24 24" aria-hidden="true"><circle cx="12" cy="12" r="12" fill="#8cc63f"/>
        <rect x="6" y="8" width="12" height="8.5" rx="1" fill="#fff"/>
        <path d="M6.5 8.6l5.5 4.2 5.5-4.2" stroke="#8cc63f" stroke-width="1.2" fill="none"/></svg>
      <span>example@email.com</span>
    </div>
    <div class="contact" style="top:167px">
      <svg viewBox="0 0 24 24" aria-hidden="true"><circle cx="12" cy="12" r="12" fill="#8cc63f"/>
        <path d="M12 5.5a4 4 0 0 0-4 4c0 3 4 8.5 4 8.5s4-5.5 4-8.5a4 4 0 0 0-4-4z" fill="#fff"/>
        <circle cx="12" cy="9.6" r="1.5" fill="#8cc63f"/></svg>
      <span>Level 1, 214 Marlowe Avenue,<br>Dunreath NO, 6120</span>
    </div>
  </div>
</section>

</body>
</html>
```